Bright Oak Collective needs updated website.

Our current website was designed on wix.com. (www.brightoakcollective.com).
We would like something a little more customized for what our company offers. Bright Oak Collective is a company specializing in connecting consumers with trustworthy and affordable service professionals. We need the website to be approachable and easy to use, while conveying our "Bright Oak" reputation.
Updates
Project Deadline Extended
Reason: Our project is now guaranteed. Please send your ideas. Thank you!
Target Market(s)
Homeowners
Industry/Entity Type
It Company
Look and feel
Each slider illustrates characteristics of the customer's brand and the style your logo design should communicate.

```html
<!DOCTYPE html>
<html lang="en">
<head>
<meta charset="utf-8">
<title>Bright Oak Collective</title>
<link rel="stylesheet" href="https://fonts.googleapis.com/css2?family=Arimo:wght@400;700&display=swap">
<style>
  :root {
    --brand-blue: #1f80d6;
    --deep-blue: #0d4a94;
    --card-blue: #4a9ae0;
    --ink: #1f1f1f;
    --tile-grey: #8e8e8e;
    --tile-text: #3e3e3e;
    --accent-red: #c90e14;
    --footer-dark: #2b2b2b;
    --white: #ffffff;
  }
  * { box-sizing: border-box; margin: 0; padding: 0; }
  html, body { width: 1200px; height: 1080px; overflow: hidden; background: var(--white); }
  body { font-family: "Arimo", Arial, sans-serif; color: var(--ink); }
  .page { position: relative; width: 1172px; height: 1080px; }

  .site-header { position: absolute; left: 0; top: 0; width: 1172px; height: 105px; background: var(--brand-blue); border-bottom: 4px solid var(--deep-blue); }
  .brand { position: absolute; left: 60px; top: 20px; height: 64px; display: flex; align-items: center; gap: 10px; }
  .brand-dot { width: 40px; height: 40px; border-radius: 50%; background: var(--white); }
  .brand-name { font-size: 24px; font-weight: 700; color: var(--white); line-height: 1; }
  .header-phone { position: absolute; left: 364px; top: 40px; font-size: 27px; font-weight: 700; color: var(--white); }
  .main-nav { position: absolute; left: 670px; top: 0; height: 101px; display: flex; align-items: center; }
  .main-nav a { color: var(--white); text-decoration: none; font-size: 18px; padding: 0 15px; position: relative; }
  .main-nav a + a::before { content: ""; position: absolute; left: -1px; top: 6px; width: 1px; height: 9px; background: rgba(255,255,255,.6); }
  .main-nav a.is-current { background: var(--white); color: var(--brand-blue); height: 101px; line-height: 108px; width: 85px; padding: 0; text-align: center; }
  .main-nav a.is-current + a::before { display: none; }

  .hero-photo { position: absolute; left: 0; top: 105px; width: 345px; height: 345px; background: linear-gradient(135deg, #c9a27a 0%, #e8d2bd 45%, #3b3a45 100%); }
  .hero-copy { position: absolute; left: 412px; top: 160px; width: 685px; text-align: center; }
  .hero-title { font-size: 30px; font-weight: 700; letter-spacing: .3px; margin-bottom: 20px; }
  .hero-text { font-size: 20.5px; line-height: 25.7px; }
  .hero-service { position: absolute; left: 412px; top: 402px; width: 650px; text-align: center; font-size: 30px; font-weight: 700; }

  .info-band { position: absolute; left: 0; top: 450px; width: 1172px; height: 291px; background: var(--brand-blue); border-top: 2px solid var(--deep-blue); }
  .info-title { position: absolute; top: 9px; width: 472px; text-align: center; color: var(--white); font-size: 23px; }
  .info-card { position: absolute; width: 472px; background: var(--card-blue); border-radius: 10px; color: var(--white); font-size: 18.3px; line-height: 22.3px; }
  .info-card::before { content: ""; position: absolute; left: 0; right: 0; top: -3px; height: 5px; border-radius: 50%; background: var(--white); }
  .about-title { left: 64px; }
  .about-card { left: 76px; top: 48px; height: 227px; padding: 8px 18px 0 20px; }
  .vision-title { left: 634px; }
  .vision-card { left: 638px; top: 45px; height: 227px; padding: 46px 18px 0 14px; }

  .network { position: absolute; left: 0; top: 768px; width: 1172px; }
  .network-title { text-align: center; font-size: 21px; font-weight: 700; }
  .tile { position: absolute; top: 50px; width: 134px; height: 133px; background: var(--tile-grey); color: var(--tile-text); font-weight: 700; font-size: 16.5px; line-height: 19.5px; display: flex; align-items: center; justify-content: center; text-align: center; }
  .tile.is-featured { background: var(--accent-red); color: var(--white); }

  .site-footer { position: absolute; left: 0; top: 993px; width: 1172px; height: 87px; background: var(--footer-dark); color: var(--white); font-size: 15px; display: flex; align-items: center; justify-content: center; gap: 10px; }
</style>
</head>
<body>
<div class="page">
  <header class="site-header">
    <div class="brand"><span class="brand-dot"></span><span class="brand-name">Bright Oak Collective</span></div>
    <div class="header-phone">1-555-014-2237</div>
    <nav class="main-nav">
      <a class="is-current" href="#">HOME</a>
      <a href="#">SERVICIES</a>
      <a href="#">ABOUT US</a>
      <a href="#">CONTACT</a>
    </nav>
  </header>

  <div class="hero-photo" role="img" aria-label="Photo of a smiling customer service agent wearing a headset"></div>
  <section class="hero-copy">
    <h1 class="hero-title">YOU CAN COUNT ON US</h1>
    <p class="hero-text">Sometimes things are just easier when you know someone in the busi-ness. That's where Bright Oak Collective comes in. Whether your Air Conditioner is on the fritz, you've got a leaky roof, or need a car sales-man you can actually trust.. Whatever it is, we connect you with Saint Louis' most reputable and affordable solutions, all at NO COST TO YOU!!</p>
  </section>
  <div class="hero-service">24/7 SERVICE: 1-555-014-2237</div>

  <section class="info-band">
    <h2 class="info-title about-title">ABOUT US</h2>
    <div class="info-card about-card">The founders of Bright Oak Collective have over 30 years in the St. Louis automotive and HVAC indus-tries. In both markets, among many others, one thing is clear: A consumer gets better service at a lower price when they know who to call. Opening up a phonebook, newspaper, or randomly selected online business could cost you hundreds, even thousands of dollars too much money. Sometimes all you really need is a Bright Oak.</div>
    <h2 class="info-title vision-title">OUR VISION</h2>
    <div class="info-card vision-card">Bright Oak Collective is now sharing their industry con-nections with everyone. It's no longer necessary to have a friend or family member in the business to get the service and prices you deserve. Bright Oak Col-lective, connecting YOU with the most reputable and affordable businesses in Saint Louis.</div>
  </section>

  <section class="network">
    <h2 class="network-title">OUR NETWORK</h2>
    <div class="tile" style="left:61px">Heating<br>Air<br>Conditioning</div>
    <div class="tile" style="left:210px">Automotive<br>Maintenance</div>
    <div class="tile is-featured" style="left:359px">Automotive<br>Sales</div>
    <div class="tile" style="left:509px">Home Repair</div>
    <div class="tile" style="left:664px">Painting</div>
    <div class="tile" style="left:813px">Chiropractic</div>
    <div class="tile" style="left:962px">Roofing</div>
  </section>

  <footer class="site-footer">
    <span>Copyright Bright Oak Company</span><span>|</span><span>Terms and Conditions</span><span>|</span><span>Contact</span>
  </footer>
</div>
</body>
</html>
```